Energieausweis
Zielgruppe
Zielgruppe sind Immobilieninteressenten - Verwendung in einem Immobilienmagazin und im Internet.
Aufgabenstellung
Ab dem 1. Mai muss in Deutschland die Energie-Effizienzklasse bei Immobilienangeboten mit veröffentlicht werden. Das kann man nüchtern in Zahlen darstellen, aber auch in einer netten Grafik. In der Anlage finden 2 von uns gekaufte Pixbarun-Bilder. Das Bild mit dem Männchen ist eine sehr nette Idee. Da wir in unserem Logo auch ein Männchen haben, bietet es sich an, ein LindenHaus-Männchen zusammen mit der bunten Grafik zu gestalten. (Das Pixbarun-Bild soll nur die Idee erklären - bitte nicht verwenden). Wenn die Grafik fertig ist, legen wir einen Pfeil zur Kennzeichnung der jeweiligen Energieklasse hinzu. Das heisst, wir haben dann für jede Energieklasse eine entsprechende Vorlage und dem richtig platzierten Pfeil. Weiter finden sie in der Anlage unser Firmenlogo zur freuen Verwendung.

```html
<!DOCTYPE html>
<html lang="de">
<head>
<meta charset="utf-8">
<title>Energieausweis – LindenHaus</title>
<link rel="stylesheet" href="https://fonts.googleapis.com/css2?family=Barlow+Semi+Condensed:wght@600;700&display=swap">
<style>
  :root {
    --frame-blue: #0f5192;
    --title-red: #e3343b;
    --paper: #ffffff;
    --track: #f4f4f4;
    --class-a: #007a3d;
    --class-b: #2ea33b;
    --class-c: #95c04e;
    --class-d: #e4dc00;
    --class-e: #fbbb07;
    --class-f: #ec6d38;
    --class-g: #e3343b;
    --marker: #919ac4;
    --mascot-tone: #1c4f95;
  }
  html, body {
    margin: 0;
    padding: 0;
    width: 848px;
    height: 1200px;
    overflow: hidden;
    background: var(--paper);
  }
  .energy-label {
    display: block;
    width: 848px;
    height: 1200px;
    font-family: "Barlow Semi Condensed", "Arial Narrow", sans-serif;
  }
  .frame { fill: var(--frame-blue); }
  .house { fill: var(--paper); }
  .headline { fill: var(--title-red); font-weight: 700; font-size: 60px; }
  .subline { fill: var(--frame-blue); font-weight: 700; font-size: 40px; }
  .track { fill: var(--track); }
  .class-bar { stroke: var(--paper); stroke-width: 2; }
  .class-letter { fill: var(--paper); font-weight: 700; font-size: 46px; text-anchor: middle; }
  .bar-a { fill: var(--class-a); }
  .bar-b { fill: var(--class-b); }
  .bar-c { fill: var(--class-c); }
  .bar-d { fill: var(--class-d); }
  .bar-e { fill: var(--class-e); }
  .bar-f { fill: var(--class-f); }
  .bar-g { fill: var(--class-g); }
  .class-marker { fill: var(--marker); }
  .mascot-area { fill: var(--mascot-tone); opacity: 0.85; }
  .brand-mark { fill: var(--frame-blue); }
  .brand-name { fill: var(--frame-blue); font-weight: 700; font-size: 40px; }
</style>
</head>
<body>
<svg class="energy-label" viewBox="0 0 848 1200" xmlns="http://www.w3.org/2000/svg">
  <rect class="frame" x="81" y="75" width="686" height="907"/>
  <polygon class="house" points="121,236 424,120 727,236 727,941 121,941"/>

  <text class="headline" x="152" y="294" textLength="546" lengthAdjust="spacingAndGlyphs">ENERGIEAUSWEIS</text>
  <text class="subline" x="152" y="336" textLength="545" lengthAdjust="spacingAndGlyphs">Berechneter Energiebedarf</text>

  <g class="scale">
    <rect class="track" x="152" y="364" width="546" height="60" rx="3"/>
    <rect class="track" x="152" y="431" width="546" height="60" rx="3"/>
    <rect class="track" x="152" y="498" width="546" height="60" rx="3"/>
    <rect class="track" x="152" y="565" width="546" height="60" rx="3"/>
    <rect class="track" x="152" y="632" width="546" height="60" rx="3"/>
    <rect class="track" x="152" y="699" width="546" height="60" rx="3"/>
    <rect class="track" x="152" y="766" width="546" height="60" rx="3"/>

    <path class="class-bar bar-a" d="M156,364 H331 L368,394 L331,424 H156 Q152,424 152,420 V368 Q152,364 156,364 Z"/>
    <path class="class-bar bar-b" d="M156,431 H361 L398,461 L361,491 H156 Q152,491 152,487 V435 Q152,431 156,431 Z"/>
    <path class="class-bar bar-c" d="M156,498 H391 L428,528 L391,558 H156 Q152,558 152,554 V502 Q152,498 156,498 Z"/>
    <path class="class-bar bar-d" d="M156,565 H421 L458,595 L421,625 H156 Q152,625 152,621 V569 Q152,565 156,565 Z"/>
    <path class="class-bar bar-e" d="M156,632 H453 L490,662 L453,692 H156 Q152,692 152,688 V636 Q152,632 156,632 Z"/>
    <path class="class-bar bar-f" d="M156,699 H483 L520,729 L483,759 H156 Q152,759 152,755 V703 Q152,699 156,699 Z"/>
    <path class="class-bar bar-g" d="M156,766 H513 L550,796 L513,826 H156 Q152,826 152,822 V770 Q152,766 156,766 Z"/>

    <text class="class-letter" x="199" y="411">A</text>
    <text class="class-letter" x="199" y="478">B</text>
    <text class="class-letter" x="199" y="545">C</text>
    <text class="class-letter" x="199" y="612">D</text>
    <text class="class-letter" x="199" y="679">E</text>
    <text class="class-letter" x="199" y="746">F</text>
    <text class="class-letter" x="199" y="813">G</text>

    <path class="class-marker" d="M553,662 L585,632 H694 Q698,632 698,636 V688 Q698,692 694,692 H585 Z"/>
    <rect class="mascot-area" role="img" aria-label="Maskottchen: laufendes Männchen mit einem kleinen Haus im Arm" x="578" y="619" width="88" height="86" rx="6"/>
  </g>

  <g class="brand">
    <rect class="brand-mark" x="282" y="872" width="30" height="30"/>
    <text class="brand-name" x="326" y="902">LindenHaus</text>
  </g>
</svg>
</body>
</html>
```